Up to the Challenge? Canadian based consulting company needs a two sided business card design

A Canadian based security risk management consulting company needs a two-sided business card design. What we do is provide advice and guidance related to emergency, security and business continuity management for small, medium and large companies to help ensure the protection of their people, assets, information, services, operations and reputation.

The final design should be simple, only one or two colours, eye catching, professional and one that makes people look at three or more times just because it looks so darn good.

I have include examples of business cards I like.

Target Market(s)

Small, medium and large companies.

Industry/Entity Type

Security

Contact Information for Business Card

Business Card Size: Standard size of 3.5" (89mm) x 2.0" (51mm) - (see full specifications and guides on PRINTA's website if required)
Card Stock: Looking to use PRINTA's Velda 32pt stock textured paper - seam colour either chili red or black
Business Name: The Harrowfield Group
Website: www.theharrowfieldgroup.example
Telephone: (555)214-0397
Name: Dana Forsythe
Position: Principle
e-mail: Dana.Forsythe@theharrowfieldgroup.example

Font styles to use
Serif

Colors
ec1f27
000000
9d9d9d
aaaaaa
606060

Requirements
Must have
• - "The Harrowfield Group" logo (see uploaded files). I have included grey scale and colour versions.
• - Business card details (as above)
Nice to have
• - One side black or grey scale.
• - Other side would likely be white.
• - Everyone likes the silver logo on the black background.
• - Small element of colour i.e. red but I'm leaning more to greyscale.
Should not have
• - A lot of colour. Keep it simple.

```html
<!DOCTYPE html>
<html lang="en">
<head>
<meta charset="utf-8">
<title>The Harrowfield Group — Business Card</title>
<link href="https://fonts.googleapis.com/css2?family=Cinzel:wght@500&family=Jost:ital,wght@1,400;1,600&family=Ubuntu:wght@400&display=swap" rel="stylesheet">
<style>
  :root {
    --backdrop: #8e8e8e;
    --card-light: #f0f0f0;
    --card-dark: #1e1e1e;
    --ink-dark: #1c1c1c;
    --brand-grey: #606060;
    --white: #ffffff;
  }
  html, body {
    margin: 0;
    padding: 0;
    width: 980px;
    height: 1200px;
    overflow: hidden;
    background: var(--backdrop);
  }
  .canvas {
    position: relative;
    width: 980px;
    height: 1200px;
  }
  .card {
    position: absolute;
    overflow: hidden;
  }
  /* Front */
  .card--front {
    left: 119px;
    top: 131px;
    width: 721px;
    height: 410px;
    background: var(--card-light);
  }
  .brand-front {
    position: absolute;
    left: 0;
    right: 0;
    top: 96px;
    text-align: center;
    font-family: "Cinzel", serif;
    font-weight: 500;
    color: var(--brand-grey);
    font-size: 38px;
    line-height: 1.12;
    letter-spacing: 1px;
  }
  .brand-front .brand-mark {
    display: block;
    width: 34px;
    height: 34px;
    margin: 0 auto 22px;
    border-radius: 50%;
    background: var(--brand-grey);
  }
  .web-band {
    position: absolute;
    left: 1px;
    right: 0;
    top: 319px;
    height: 63px;
    background: var(--ink-dark);
    display: flex;
    align-items: center;
    justify-content: center;
    font-family: "Jost", sans-serif;
    font-style: italic;
    font-weight: 400;
    font-size: 26px;
    color: var(--white);
    letter-spacing: 0.3px;
  }
  /* Back */
  .card--back {
    left: 119px;
    top: 710px;
    width: 714px;
    height: 413px;
    background: var(--card-dark);
  }
  .brand-back {
    position: absolute;
    left: 30px;
    width: 230px;
    top: 145px;
    text-align: center;
    font-family: "Cinzel", serif;
    font-weight: 500;
    font-size: 27px;
    line-height: 1.2;
    color: var(--white);
  }
  .person {
    position: absolute;
    right: 34px;
    top: 40px;
    text-align: right;
    font-family: "Jost", sans-serif;
    font-style: italic;
    color: var(--white);
  }
  .person__name {
    margin: 0;
    font-weight: 600;
    font-size: 42px;
    line-height: 1;
    padding-right: 68px;
  }
  .person__role {
    margin: 6px 0 0;
    font-weight: 400;
    font-size: 30px;
    line-height: 1;
  }
  .contact-row {
    position: absolute;
    left: 307px;
    right: 0;
    height: 57px;
    background: var(--card-light);
    display: flex;
    align-items: center;
    padding-left: 18px;
    box-sizing: border-box;
    font-family: "Ubuntu", sans-serif;
    color: var(--ink-dark);
  }
  .contact-row--phone { top: 246px; font-size: 18px; }
  .contact-row--email { top: 316px; font-size: 15px; }
  .contact-row svg {
    flex: none;
    margin-right: 14px;
  }
</style>
</head>
<body>
<div class="canvas">

  <section class="card card--front" aria-label="Business card front">
    <div class="brand-front">
      <span class="brand-mark"></span>
      The Harrowfield<br>Group
    </div>
    <div class="web-band">www.theharrowfieldgroup.example</div>
  </section>

  <section class="card card--back" aria-label="Business card back">
    <div class="brand-back">The Harrowfield<br>Group</div>

    <div class="person">
      <p class="person__name">Dana Forsythe</p>
      <p class="person__role">Principle</p>
    </div>

    <div class="contact-row contact-row--phone">
      <svg width="26" height="26" viewBox="0 0 24 24" aria-hidden="true">
        <path fill="#1c1c1c" d="M6.6 10.8c1.4 2.8 3.8 5.1 6.6 6.6l2.2-2.2c.3-.3.7-.4 1-.2 1.1.4 2.3.6 3.6.6.6 0 1 .4 1 1V20c0 .6-.4 1-1 1C10.6 21 3 13.4 3 4c0-.6.4-1 1-1h3.5c.6 0 1 .4 1 1 0 1.3.2 2.5.6 3.6.1.3 0 .7-.2 1L6.6 10.8z"/>
      </svg>
      <span>(555)214-0397</span>
    </div>

    <div class="contact-row contact-row--email">
      <svg width="30" height="32" viewBox="0 0 30 32" aria-hidden="true" fill="none" stroke="#1c1c1c" stroke-width="1.6">
        <rect x="2" y="12" width="26" height="18"/>
        <path d="M2 12l13 10 13-10"/>
        <path d="M2 30l10-9M28 30l-10-9"/>
        <path d="M7 15V3h16v12"/>
        <path d="M10 7h10M10 10h10"/>
      </svg>
      <span>Dana.Forsythe@theharrowfieldgroup.example</span>
    </div>
  </section>

</div>
</body>
</html>
```